Kelvo Brook Website

Design and implement (fully coded and ready to launch) website for a professional services company - please see the documents attached and send us an email if there are any questions
Target Market(s)
Market to potential clients about the services we offer and be able to reach us for any consulting opportunities
Industry/Entity Type
Professional Service
Coding
Coded - Design and coding required
Number of Pages Required
3 page
Requirements
Must have
- Single page website design that is SEO optimized
Blog Post
Contact US page
Cool images/ logos for the service offering - not fill the website with text/content
Must be professional looking website
Coded website should also look great on different screens - mobile, tablets etc
Nice to have
- Choose easy neutral colors that compliment the logo colors. Having said that don't use every color in the logo for the website design.
Should not have
- Too many colors and several various different fonts

```html
<!DOCTYPE html>
<html lang="en">
<head>
<meta charset="utf-8">
<title>Kelvo Brook — Data Engineering &amp; Cloud Consulting</title>
<link rel="stylesheet" href="https://fonts.googleapis.com/css2?family=Poppins:wght@400;500;600&display=swap">
<style>
:root{
  --blue:#0b5cb3;
  --blue-deep:#084f9f;
  --blue-light:#1a78d0;
  --orange:#f7711f;
  --red:#e63a26;
  --ink:#1c1c1c;
  --muted:#8a8a8a;
  --line:#e8e8e8;
  --field:#f3f5f6;
  --soft:#f5f6f8;
  --white:#ffffff;
}
*{margin:0;padding:0;box-sizing:border-box}
html,body{width:1200px;height:3258px;overflow:hidden}
body{position:relative;background:var(--white);font-family:"Poppins",sans-serif;color:var(--ink)}
.abs{position:absolute}
section,header,footer{position:absolute;left:0;width:1200px}
.btn{position:absolute;display:flex;align-items:center;justify-content:center;border-radius:16px;color:#fff;font-size:10.5px;font-weight:500;background:linear-gradient(90deg,var(--orange),var(--red));text-decoration:none}
.eyebrow{position:absolute;font-size:10px;font-weight:500;color:var(--red);line-height:14px}
.center{left:0;width:1200px;text-align:center}
.h2{position:absolute;font-size:21px;font-weight:500;line-height:26px}
.body-text{font-size:10.5px;line-height:16.3px;color:var(--muted)}

/* header */
.site-header{top:0;height:119px}
.topbar-rule{position:absolute;left:470px;right:0;top:30px;border-top:1px solid var(--line)}
.top-email{position:absolute;left:718px;top:9px;font-size:9.5px;color:var(--muted)}
.top-call{position:absolute;left:834px;top:7px;font-size:13px;font-weight:500}
.brand{position:absolute;left:253px;top:38px;display:flex;align-items:center;gap:8px;font-size:17px;font-weight:600;color:var(--ink)}
.brand-dot{width:14px;height:14px;border-radius:50%;background:var(--red)}
.nav{position:absolute;top:55px;font-size:11px;color:var(--ink)}
.nav.active{color:var(--blue)}
.social-dot{position:absolute;width:32px;height:32px;border-radius:50%;background:var(--blue)}

/* hero */
.hero{top:94px;height:469px;background:linear-gradient(180deg,#0a5fb7 0%,#0b62b8 50%,#0a55a8 100%);overflow:hidden}
.hero-title{position:absolute;top:66px;font-size:28px;font-weight:500;line-height:31px;color:#fff}
.hero-sub{position:absolute;top:140px;font-size:10.5px;line-height:16px;color:#e5eefb}
.globe{position:absolute;left:228px;top:272px;width:728px;height:420px;border-radius:50%;background:radial-gradient(ellipse at 50% 40%,#2b8fe0 0%,#1a74cc 45%,#0c5fb5 75%);opacity:.9}

/* services */
.services{top:563px;height:385px}
.services .eyebrow{left:253px;top:71px}
.services .h2{left:253px;top:98px;font-size:21px;line-height:23px;text-align:left}
.service{position:absolute;top:189px;width:215px}
.service svg{display:block;width:40px;height:40px}
.service h3{margin-top:14px;font-size:13px;font-weight:500;line-height:16px}
.service p{margin-top:7px}
.service .more{color:var(--blue)}

/* about */
.about{top:948px;height:375px}
.about-photo{position:absolute;left:0;top:0;width:550px;height:375px;background:linear-gradient(120deg,#2a2d30 0%,#6d6a62 45%,#c9c3b6 75%,#8e8a80 100%)}
.about .eyebrow{left:601px;top:44px}
.about .h2{left:601px;top:71px;font-size:21px;line-height:23px}
.about-copy{position:absolute;left:601px;top:132px;width:350px}
.about-copy p+p{margin-top:16px}

/* technology */
.tech{top:1323px;height:302px}
.tech .eyebrow{top:71px}
.tech .h2{top:97px}
.tech-name{position:absolute;top:185px;height:32px;display:flex;align-items:center;justify-content:center;font-size:24px;font-weight:500;color:#b3b3b3}

/* founder */
.founder{top:1625px;height:375px;overflow:hidden}
.founder-photo{position:absolute;inset:0;background:linear-gradient(90deg,#c4cbd2 0%,#d6dbe0 35%,#9ca6ae 60%,#b7bfc6 80%,#dfe3e6 100%)}
.founder-card{position:absolute;left:253px;top:50px;width:297px;height:275px;background:#fff}
.founder-card h3{position:absolute;left:38px;top:32px;font-size:26px;font-weight:500;line-height:30px}
.founder-card .role{position:absolute;left:38px;top:64px;font-size:10.5px;color:var(--red)}
.founder-card .body-text{position:absolute;left:38px;top:97px;width:225px}

/* quote */
.quote{top:2000px;height:466px}
.quote .eyebrow{top:72px}
.quote .h2{top:97px}
.field{position:absolute;height:29px;border-radius:15px;background:var(--field);font-size:9.5px;color:var(--muted);padding:9px 18px}
.field.area{height:91px;border-radius:12px}

/* articles */
.articles{top:2466px;height:792px;background:var(--soft)}
.articles-bg{position:absolute;inset:0 0 auto 0;height:420px;background:linear-gradient(160deg,#e9ecef 0%,#f5f6f8 40%,#eef0f2 100%)}
.articles .eyebrow{top:72px}
.articles .h2{top:98px}
.post{position:absolute;top:150px;width:219px}
.post-img{height:125px}
.post-meta{margin-top:18px;font-size:8.5px;color:var(--red)}
.post h3{margin-top:6px;font-size:12.5px;font-weight:500;line-height:17px}
.post h3.link{color:var(--blue);text-decoration:underline}
.cta{position:absolute;left:253px;top:420px;width:694px;height:100px;background:var(--blue);border-radius:3px}
.cta p{position:absolute;left:38px;top:38px;font-size:18px;font-weight:500;color:#fff}
.foot-title{position:absolute;top:587px;font-size:12.5px;font-weight:500}
.foot-call{position:absolute;left:253px;top:609px;font-size:19px;font-weight:500}
.foot-email{position:absolute;left:253px;top:634px;font-size:10.5px;color:var(--muted)}
.foot-link{position:absolute;font-size:9.5px;color:var(--muted)}
.foot-link.active{color:var(--blue)}
.subscribe{position:absolute;left:728px;top:613px;width:219px;height:30px;border:1px solid #cfd3d8;border-radius:15px;font-size:9.5px;color:var(--muted);padding:8px 17px}
.copyright{position:absolute;left:253px;top:744px;font-size:9px;color:var(--muted)}
</style>
</head>
<body>

<header class="site-header">
  <div class="topbar-rule"></div>
  <span class="top-email">e. hello@kelvobrook.com</span>
  <span class="top-call">Call. 800.555.0142</span>
  <a class="brand"><span class="brand-dot"></span>Kelvo Brook</a>
  <span class="nav active" style="left:527px">Home</span>
  <span class="nav" style="left:585px">Company</span>
  <span class="nav" style="left:664px">Services</span>
  <span class="nav" style="left:735px">Resources</span>
  <a class="btn" style="left:816px;top:47px;width:87px;height:31px">Contact</a>
  <span class="social-dot" style="left:915px;top:46px" aria-label="Social profile"></span>
</header>

<section class="hero">
  <div class="globe" role="img" aria-label="Glowing network globe with connected data points"></div>
  <h1 class="hero-title center">Our work is presentation<br>of our capabilities.</h1>
  <p class="hero-sub center">Ut enim ad minima veniam, quis nostrum exercitationem ullam corporis<br>suscipit laboriosam, nisi ut aliquid ex ea.</p>
  <a class="btn" style="left:544px;top:199px;width:112px;height:32px">Explore More</a>
</section>

<section class="services">
  <span class="eyebrow">Kelvo Brook provides end to end services</span>
  <h2 class="h2">We work with business &amp; provide solution to<br>client with their business problem</h2>

  <article class="service" style="left:253px">
    <svg viewBox="0 0 40 40" fill="none" stroke="#1a6cc4" stroke-width="1.5"><path d="M11 22a6 6 0 0 1 1-12 9 9 0 0 1 17 2 5 5 0 0 1 0 10z"/><path d="M14 22v8M20 18v14M26 22v8"/><circle cx="14" cy="32" r="2"/><circle cx="20" cy="34" r="2"/><circle cx="26" cy="32" r="2"/></svg>
    <h3>Platform Architecture</h3>
    <p class="body-text">Excepteur sint occaecat cupidatat non proident, sunt in culpa qui officia deserunt mollit anim ... <span class="more">(+)</span></p>
  </article>
  <article class="service" style="left:491px">
    <svg viewBox="0 0 40 40" fill="none" stroke="#1a6cc4" stroke-width="1.5"><rect x="11" y="11" width="18" height="18" rx="2"/><rect x="15" y="15" width="10" height="10"/><path d="M15 6v5M20 6v5M25 6v5M15 29v5M20 29v5M25 29v5M6 15h5M6 20h5M6 25h5M29 15h5M29 20h5M29 25h5"/></svg>
    <h3>Data Engineering</h3>
    <p class="body-text">Excepteur sint occaecat cupidatat non proident, sunt in culpa qui officia deserunt mollit anim id ... <span class="more">(+)</span></p>
  </article>
  <article class="service" style="left:728px">
    <svg viewBox="0 0 40 40" fill="none" stroke="#1a6cc4" stroke-width="1.5"><rect x="6" y="6" width="28" height="8" rx="1"/><rect x="6" y="16" width="28" height="8" rx="1"/><rect x="6" y="26" width="28" height="8" rx="1"/><path d="M10 10h6M10 20h6M10 30h6M22 8l-2 4M26 10l2 0"/></svg>
    <h3>Cloud Developments</h3>
    <p class="body-text">Excepteur sint occaecat cupidatat non proident, sunt in culpa qui officia deserunt mollit anim id ... <span class="more">(+)</span></p>
  </article>
</section>

<section class="about">
  <div class="about-photo" role="img" aria-label="Colleagues talking across a meeting table with a laptop"></div>
  <span class="eyebrow">What we are</span>
  <h2 class="h2">Understanding the client's<br>business and industry</h2>
  <div class="about-copy body-text">
    <p>Kelvo Brook is a company which intends to be in front of the client's needs, deeply understanding clients' business and delivering and optimizing solutions from the initial phase of scoping the requirements, up to the final delivery, maintenance and continuous upgrade.</p>
    <p>Kelvo Brook focuses always from the customer perspective to grasp their business need for the IT solutions they deliver.</p>
  </div>
  <a class="btn" style="left:601px;top:297px;width:87px;height:30px">Company</a>
</section>

<section class="tech">
  <span class="eyebrow center">Technology</span>
  <h2 class="h2 center">Our technology expertise</h2>
  <span class="tech-name" style="left:202px;width:155px">Hollow Stack</span>
  <span class="tech-name" style="left:392px;width:112px">Emberly</span>
  <span class="tech-name" style="left:534px;width:154px">Cirrusline</span>
  <span class="tech-name" style="left:722px;width:134px">Quillstream</span>
  <span class="tech-name" style="left:885px;width:113px">Cobaltia</span>
</section>

<section class="founder">
  <div class="founder-photo" role="img" aria-label="Two colleagues reviewing work on a tablet in a bright office"></div>
  <div class="founder-card">
    <h3>Oren Halvik</h3>
    <span class="role">(Founded Kelvo Brook)</span>
    <p class="body-text">Oren manages all the client interactions and engineering team at Kelvo Brook. Oren has over 15 years of experience in the technology before he founded Kelvo Brook. He managed development ...</p>
    <a class="btn" style="left:38px;top:206px;width:87px;height:31px">Read More</a>
  </div>
</section>

<section class="quote">
  <span class="eyebrow center">Get a free Quote</span>
  <h2 class="h2 center">Take the next step.</h2>
  <div class="field" style="left:376px;top:157px;width:217px">Enter your Name</div>
  <div class="field" style="left:607px;top:157px;width:217px">Email</div>
  <div class="field" style="left:376px;top:200px;width:217px">Phone</div>
  <div class="field" style="left:607px;top:200px;width:217px">Subject</div>
  <div class="field area" style="left:376px;top:243px;width:448px">Message ...</div>
  <a class="btn" style="left:556px;top:362px;width:88px;height:30px">Read More</a>
</section>

<section class="articles">
  <div class="articles-bg" role="img" aria-label="Faint architectural facade background"></div>
  <span class="eyebrow center">Latest articles</span>
  <h2 class="h2 center">Latest articles to enrich knowledge</h2>

  <article class="post" style="left:253px">
    <div class="post-img" role="img" aria-label="Close-up of an ice crystal on a blue background" style="background:linear-gradient(135deg,#8fb0c8,#c9d7e0 55%,#6d8aa2)"></div>
    <p class="post-meta">13 Mar 2020 &nbsp;|&nbsp; By Admin</p>
    <h3 class="link">Migrate your SQL database to Frostvault using Relaylane.</h3>
  </article>
  <article class="post" style="left:491px">
    <div class="post-img" role="img" aria-label="Laptop showing code beside a pencil cup" style="background:linear-gradient(135deg,#6d4c33,#2b2f36 50%,#4a5560)"></div>
    <p class="post-meta">13 Mar 2020 &nbsp;|&nbsp; By Admin</p>
    <h3>Load, display, and write data using Brickwell and ...</h3>
  </article>
  <article class="post" style="left:728px">
    <div class="post-img" role="img" aria-label="Striped glass building against a cloudy sky" style="background:linear-gradient(120deg,#a9c2d6,#dfe7ee 45%,#5f6c77)"></div>
    <p class="post-meta">13 Mar 2020 &nbsp;|&nbsp; By Admin</p>
    <h3>Connect Insight Desk to your Frostvault Data Warehouse.</h3>
  </article>

  <div class="cta">
    <p>We're ready to help you transform.</p>
    <a class="btn" style="left:518px;top:35px;width:138px;height:30px">Contact Us Today!</a>
  </div>

  <footer>
    <h4 class="foot-title" style="left:253px">Kelvo Brook LLC</h4>
    <span class="foot-call">Call. 800.555.0142</span>
    <span class="foot-email">e. hello@kelvobrook.com</span>
    <span class="social-dot" style="left:253px;top:655px" aria-label="Social profile"></span>

    <h4 class="foot-title" style="left:491px">Quick Link</h4>
    <span class="foot-link active" style="left:491px;top:611px">Home</span>
    <span class="foot-link" style="left:491px;top:633px">Company</span>
    <span class="foot-link" style="left:491px;top:656px">Services</span>
    <span class="foot-link" style="left:491px;top:678px">Resources</span>
    <span class="foot-link" style="left:491px;top:701px">Contact</span>
    <span class="foot-link" style="left:580px;top:611px">Terms &amp; Conditions</span>
    <span class="foot-link" style="left:580px;top:633px">Privacy Policy</span>
    <span class="foot-link" style="left:580px;top:656px">Support</span>

    <h4 class="foot-title" style="left:728px">Subscribe Us</h4>
    <div class="subscribe">Name@email.com</div>
    <svg class="abs" style="left:924px;top:622px" width="12" height="12" viewBox="0 0 12 12" fill="none" stroke="#f7711f" stroke-width="1.2"><circle cx="6" cy="6" r="5.2"/><path d="M3.5 6h5M6.5 4l2 2-2 2"/></svg>

    <p class="copyright">© 2019 Kelvo Brook LLC.</p>
  </footer>
</section>

</body>
</html>
```